Letterhead for new real estate company in South Africa named Tallowick

A letterhead with the directors and company details to be editable as these changes often

Target Market(s)

In line with our logo brief and our newly designed logo and corporate fee

Industry/Entity Type

Real Estate

Requirements
Must have
• Details as per the sample letterhead provided.

```html
<!DOCTYPE html>
<html lang="en">
<head>
<meta charset="utf-8">
<title>Tallowick Letterhead</title>
<link rel="stylesheet" href="https://fonts.googleapis.com/css2?family=Figtree:wght@400;500;700&display=swap">
<style>
  :root {
    --brand-green: #2fae6f;
    --earth-brown: #776753;
    --ink: #1d1d1d;
    --director-red: #d42a2a;
    --faint-green: #e3f3ea;
    --paper: #ffffff;
  }
  * { margin: 0; padding: 0; box-sizing: border-box; }
  html, body { width: 927px; height: 1200px; overflow: hidden; background: var(--paper); }
  body { font-family: "Figtree", Arial, sans-serif; color: var(--ink); }
  .letterhead { position: relative; width: 927px; height: 1200px; overflow: hidden; }
  .top-rule { position: absolute; top: 0; left: 0; width: 100%; height: 8px; background: var(--earth-brown); }
  .brand {
    position: absolute; top: 46px; left: 0; width: 100%;
    display: flex; justify-content: center; align-items: center; gap: 14px;
  }
  .brand-dot { width: 34px; height: 34px; border-radius: 50%; background: var(--brand-green); }
  .brand-name {
    font-size: 46px; font-weight: 500; letter-spacing: 1px;
    color: var(--brand-green); text-transform: uppercase; line-height: 1;
  }
  .backdrop-mark {
    position: absolute; left: 470px; top: 520px;
    width: 480px; height: 480px; border-radius: 50%;
    background: var(--faint-green); opacity: 0.6;
  }
  .footer-rule { position: absolute; top: 1046px; left: 0; width: 100%; height: 1.5px; background: var(--brand-green); }
  .company-details {
    position: absolute; left: 27px; top: 1061px;
    font-size: 13px; line-height: 16.5px;
  }
  .company-details .contact { margin-top: 7px; }
  .company-details .contact + .contact { margin-top: 7px; }
  .directors {
    position: absolute; right: 27px; top: 1061px; text-align: right;
    font-size: 13px; line-height: 16.5px;
  }
  .directors-title { color: var(--director-red); font-weight: 700; margin-bottom: 6px; }
  .director-name { font-weight: 700; }
  .franchise-note { margin-top: 19px; }
  .bottom-band { position: absolute; left: 0; bottom: 0; width: 100%; height: 26px; background: var(--brand-green); }
</style>
</head>
<body>
  <div class="letterhead">
    <div class="top-rule"></div>

    <header class="brand">
      <span class="brand-dot"></span>
      <span class="brand-name">Tallowick</span>
    </header>

    <div class="backdrop-mark"></div>

    <div class="footer-rule"></div>

    <footer>
      <div class="company-details">
        <p>Highveld Estates (Pty) Ltd Va Keystone Homes Northgate, Reg No: 2019/448207/07</p>
        <p>Shop 12B, Marula Square, Corner Acacia Drive &amp; Fern Street</p>
        <p>Northgate, South Africa</p>
        <p class="contact">Tel: 010 555 0142</p>
        <p class="contact">Web: www keystonehomes.co.za</p>
      </div>

      <div class="directors">
        <p class="directors-title">Directors:</p>
        <p class="director-name">M Venter</p>
        <p class="director-name">LJ Carter-Brooks</p>
        <p class="franchise-note">Each franchise is independently owned and operated</p>
      </div>
    </footer>

    <div class="bottom-band"></div>
  </div>
</body>
</html>
```